Toddler Music Class Bussiness Needs Web Design

We are a small start up called "WeeBopplings" providing music classes to kids from 6 months to 3 years of age. Kids are instructor led and learn to play a variety of instruments (e.g. drums, tambourines, ukulele's, castanets, etc..), develop coordination and rhythm, and stimulate mental development while having a blast of a time along with other kids and their parents.
The website design needs to be clever, have clean lines, simple modern font, original, fun and colourful and professional. It will need to look good when viewed across different devices and be able to scale well when resized.
This website needs to convey the message that the classes will be enjoyed by parents and children, be safe and contribute to the development of their children.
We have a logo that needs to be incorporated into the design and lead the approach. There will be a number of web pages illustrated in the site map accompanied with this project. The winning bid will have a design that represents a number of pages of the website e.g. 4/5 of the pages

****** commercial in confidence ******
Updates

Reason: Hi Designers, appreciate the design submissions thus far. We have decided to extend tge deadline due to requests from designers :)

Just wanted to say thanks for the designs sent through, there are a few good ones (:

In general we are looking for a little more of a playful approach and have included a few variations on the logos to encourage different design approaches.

Feel free to have a play!!

Target Market(s)

Parents in Australia (multicultural) aged 25 to 45

Industry/Entity Type

Learn

Requirements
Must have
• The website design needs to be clever, have clean lines, simple modern font, original, fun and colourful and professional. It will need to look good when viewed across different devices and be able to scale well when resized.
We have a logo that needs to be incorporated into the design and lead the approach.

```html
<!DOCTYPE html>
<html lang="en">
<head>
<meta charset="utf-8">
<title>WeeBopplings – About Us</title>
<link rel="stylesheet" href="https://fonts.googleapis.com/css2?family=Open+Sans:wght@400;600;700&family=Sniglet:wght@400;800&display=swap">
<style>
  :root {
    --purple: #8e3d9b;
    --purple-dark: #6d2a78;
    --blue: #0f6fb8;
    --green: #22b14c;
    --orange: #f7941d;
    --red: #ed1c24;
    --coral: #f2664a;
    --coral-dark: #c9462d;
    --text: #555555;
    --grey: #8a8a8a;
    --rule: #bdbdbd;
    --white: #ffffff;
  }
  * { box-sizing: border-box; margin: 0; padding: 0; }
  html, body { width: 1200px; height: 980px; overflow: hidden; background: var(--white); }
  body { position: relative; font-family: "Open Sans", Arial, sans-serif; color: var(--text); }

  .rainbow-bar { position: absolute; top: 0; left: 0; width: 1200px; height: 5px; display: flex; }
  .rainbow-bar span { height: 100%; }

  .brand { position: absolute; left: 115px; top: 62px; display: flex; align-items: center; gap: 12px; }
  .brand-dot { width: 34px; height: 34px; border-radius: 50%; background: var(--purple); }
  .brand-name { font-size: 38px; font-weight: 700; color: var(--purple); letter-spacing: 0.5px; }

  .enrol { position: absolute; right: 324px; top: 92px; text-align: right; color: var(--purple); font-weight: 700; }
  .enrol-label { font-size: 16px; line-height: 22px; }
  .enrol-phone { font-size: 25px; line-height: 30px; }
  .enrol-or { position: absolute; left: 888px; top: 106px; font-size: 14px; font-weight: 700; color: var(--grey); }

  .btn-forms {
    position: absolute; left: 918px; top: 87px; width: 182px; height: 53px;
    background: var(--purple); border-radius: 14px; box-shadow: inset 0 -4px 0 var(--purple-dark);
    color: var(--white); font-size: 16px; font-weight: 700; text-align: center; line-height: 49px;
  }

  .main-nav {
    position: absolute; left: 100px; top: 161px; width: 1000px; height: 42px;
    background: var(--purple); border-radius: 6px; box-shadow: inset 0 -4px 0 var(--purple-dark);
    display: flex;
  }
  .main-nav a {
    color: var(--white); text-decoration: none; font-size: 16px; font-weight: 700;
    line-height: 38px; padding: 0 17px 0 18px; border-right: 1px solid var(--purple-dark);
  }

  .page-title { position: absolute; left: 113px; top: 224px; font-family: "Sniglet", "Comic Sans MS", cursive; font-weight: 800; font-size: 48px; color: var(--green); }
  .copy { font-size: 14.5px; line-height: 22px; }
  .intro { position: absolute; left: 113px; top: 289px; width: 545px; }
  .intro p + p { margin-top: 15px; }

  .photo { position: absolute; }
  .photo-garden { left: 701px; top: 240px; width: 399px; height: 265px; background: linear-gradient(160deg, #8a6b3e 0%, #5f7a3a 45%, #7b7c6c 75%, #a8a59b 100%); }
  .photo-child { left: 788px; top: 531px; width: 312px; height: 230px; background: linear-gradient(180deg, #f7f7f7 0%, #f0e4da 55%, #e9e9e9 100%); }

  .section-title { position: absolute; left: 113px; top: 533px; font-size: 25px; font-weight: 600; color: var(--green); }
  .section-body { position: absolute; left: 113px; top: 567px; width: 625px; }
  .list-title { position: absolute; left: 114px; top: 650px; font-size: 14.5px; font-weight: 700; }
  .feature-list { position: absolute; left: 127px; top: 673px; list-style: none; }
  .feature-list li::before { content: "•"; font-size: 10px; margin-right: 5px; vertical-align: 2px; }

  .btn-cta {
    position: absolute; left: 100px; top: 792px; width: 314px; height: 71px;
    background: var(--coral); border-radius: 14px; box-shadow: inset 0 -6px 0 var(--coral-dark);
    color: var(--white); font-family: "Sniglet", "Comic Sans MS", cursive; font-size: 24px;
    text-align: center; line-height: 66px;
  }

  .site-footer { position: absolute; left: 100px; top: 898px; width: 1001px; border-top: 1px solid var(--rule); padding-top: 5px; font-size: 14px; }
</style>
</head>
<body>
  <div class="rainbow-bar">
    <span style="width:140px;background:var(--purple)"></span>
    <span style="width:228px;background:var(--blue)"></span>
    <span style="width:227px;background:var(--green)"></span>
    <span style="width:227px;background:var(--orange)"></span>
    <span style="width:228px;background:var(--red)"></span>
    <span style="width:150px;background:var(--purple)"></span>
  </div>

  <header>
    <div class="brand"><span class="brand-dot"></span><span class="brand-name">WeeBopplings</span></div>
    <div class="enrol">
      <div class="enrol-label">enrol today</div>
      <div class="enrol-phone">call 8123-4567</div>
    </div>
    <span class="enrol-or">OR</span>
    <a class="btn-forms">download forms</a>
    <nav class="main-nav">
      <a>Home</a><a>About Us</a><a>Classes</a><a>Enrol</a><a>Contact Us</a><a>Merchandise</a>
    </nav>
  </header>

  <main>
    <h1 class="page-title">About Us</h1>
    <div class="intro copy">
      <p>Lorem ipsum dolor sit amet, consectetur adipiscing elit. Aliquam cursus sem quis ipsum aliquam, quis sollicitudin ante commodo. Maecenas consectetur arcu vitae est vulputate malesuada.</p>
      <p>Praesent bibendum nisi risus. Suspendisse potenti. Praesent risus lorem, pulvinar id vulputate vitae, iaculis rutrum lacus. Donec tempor luctus quam vitae mattis. Nullam bibendum non nulla aliquet pulvinar. Fusce tempus magna ut erat bibendum rutrum. Sed placerat pellentesque felis, ac ultricies nunc cursus quis. Vestibulum eleifend, purus in lobortis auctor, lacus metus ullamcorper justo, dictum viverra lectus magna a lacus.</p>
    </div>
    <div class="photo photo-garden" role="img" aria-label="Photo of a kindergarten garden fence decorated with colourful flowers and a ladybird"></div>

    <h2 class="section-title">Lorem Ipsum Dolor sit Amet</h2>
    <p class="section-body copy">Fusce commodo, metus in vestibulum lobortis, enim velit tristique sem, eget pharetra nisi mi vitae odio. Vestibulum dapibus metus tellus, eget dignissim massa malesuada ac. Pellentesque habitant morbi tristique senectus et netus et malesuada fames ac turpis egestas.</p>
    <p class="list-title">Phasellus vel magna sed:</p>
    <ul class="feature-list copy">
      <li>Donec euismod odio at erat adipiscing rhoncus.</li>
      <li>Ut venenatis magna sodales urna interdum, et euismod nibh pretium.</li>
      <li>Donec molestie libero nec dignissim dapibus.</li>
      <li>Ut iaculis lectus vel blandit fringilla.</li>
    </ul>
    <div class="photo photo-child" role="img" aria-label="Photo of a toddler playing a colourful xylophone"></div>

    <a class="btn-cta">Lorem ipsum dolor?</a>
  </main>

  <footer class="site-footer">© WeeBopplings, 2014</footer>
</body>
</html>
```